Birchford Realty Business Card

Business Card:

Somewhere on front of card, please include Broker License Number: 5839162

Website is BirchfordRealty.example

Address is:
7218 Crestover Ave E
Saginaw, MI 48271

I'll let you use creative freedom on the rest; we obviously need Name, Title, Email (@BirchfordRealty.example), Office Phone, Cell Phone.

Don't want any special die-cutting, just a standard size business card.

On the back, include a place for the date and time of an appointment to be written in pen.

Requirements
Must have
• Our logo, attached to email.

```html
<!DOCTYPE html>
<html lang="en">
<head>
<meta charset="utf-8">
<title>Birchford Realty Business Card</title>
<link href="https://fonts.googleapis.com/css2?family=Arimo:wght@400;700&family=Roboto+Slab:wght@400;700&display=swap" rel="stylesheet">
<style>
  :root{
    --bg:#2a2a2c;
    --card-black:#1c1c1d;
    --panel-grey:#c9c9cb;
    --brand-blue:#302f86;
    --ink:#1a1a1a;
    --white:#ffffff;
  }
  *{margin:0;padding:0;box-sizing:border-box}
  html,body{width:1200px;height:1200px;overflow:hidden;background:var(--bg)}
  .canvas{position:relative;width:1200px;height:1200px}
  .card{position:absolute;left:250px;width:700px;height:400px;overflow:hidden;box-shadow:0 10px 30px rgba(0,0,0,.45)}
  .card--front{top:150px;display:flex}
  .card--back{top:650px;background:var(--card-black)}

  /* front */
  .contact-panel{position:relative;width:290px;flex:none;height:100%;background:var(--panel-grey);padding:26px 20px}
  .person-name{font-family:"Arimo",sans-serif;font-weight:400;font-size:27px;color:var(--ink);letter-spacing:-.5px;line-height:1;white-space:nowrap}
  .person-name strong{color:var(--brand-blue);font-weight:700}
  .person-title{font-family:"Arimo",sans-serif;font-size:16px;color:var(--ink);margin-top:4px}
  .contact-list{list-style:none;margin-top:112px}
  .contact-list li{display:flex;align-items:center;gap:8px;font-family:"Arimo",sans-serif;font-size:12px;color:var(--ink);height:28px;letter-spacing:-.2px;white-space:nowrap}
  .contact-list svg{width:22px;height:22px;flex:none}
  .skyline{position:absolute;left:0;bottom:0;width:100%;height:80px;background:linear-gradient(180deg,#4a48a0,var(--brand-blue))}
  .brand-panel{position:relative;flex:1;background:radial-gradient(circle at 50% 35%,#2a2a2b,var(--card-black) 70%)}
  .license{position:absolute;top:22px;right:22px;font-family:"Roboto Slab",serif;font-size:11px;color:var(--white)}
  .brand-name{position:absolute;left:0;right:0;top:168px;text-align:center;font-family:"Arimo",sans-serif;font-weight:700;font-size:42px;color:var(--brand-blue);letter-spacing:-.5px;white-space:nowrap}
  .address{position:absolute;left:20px;right:20px;bottom:22px;text-align:right;font-family:"Roboto Slab",serif;font-size:14px;color:var(--white);white-space:nowrap}

  /* back */
  .back-curve{position:absolute;inset:0}
  .back-brand{position:absolute;left:30px;top:60px;font-family:"Arimo",sans-serif;font-weight:700;font-size:30px;color:var(--brand-blue)}
  .appt-field{position:absolute;display:flex;align-items:flex-end;gap:6px;font-family:"Roboto Slab",serif;font-size:12px;color:var(--ink);letter-spacing:.3px}
  .appt-field .fill{flex:1;border-bottom:1.5px dotted var(--ink);height:12px}
  .field-date{left:445px;right:30px;top:125px}
  .field-time{left:455px;right:30px;top:153px}
  .field-desc{left:530px;right:30px;top:187px}
  .desc-line{position:absolute;left:30px;right:30px;border-bottom:1.5px dotted var(--ink)}
</style>
</head>
<body>
<main class="canvas">

  <section class="card card--front" aria-label="Business card front">
    <div class="contact-panel">
      <h1 class="person-name">DANA <strong>WHITLOW</strong></h1>
      <p class="person-title">Director</p>
      <ul class="contact-list">
        <li>
          <svg viewBox="0 0 22 22" aria-hidden="true"><circle cx="11" cy="11" r="9.5" fill="none" stroke="#1a1a1a" stroke-width="1.6"/><path d="M7.5 6.5l2 -0.5 1 2.5-1.2 1c.6 1.3 1.6 2.3 2.9 2.9l1-1.2 2.5 1-.5 2c-4 .3-8-3.7-7.7-7.7z" fill="#1a1a1a"/></svg>
          000-0000-0000
        </li>
        <li>
          <svg viewBox="0 0 22 22" aria-hidden="true"><circle cx="11" cy="11" r="9.5" fill="none" stroke="#1a1a1a" stroke-width="1.6"/><rect x="8" y="5.5" width="6" height="11" rx="1" fill="none" stroke="#1a1a1a" stroke-width="1.4"/></svg>
          90000-00000
        </li>
        <li>
          <svg viewBox="0 0 22 22" aria-hidden="true"><circle cx="11" cy="11" r="9.5" fill="none" stroke="#1a1a1a" stroke-width="1.6"/><rect x="6" y="7.5" width="10" height="7" fill="#1a1a1a"/><path d="M6 7.5l5 4 5-4" fill="none" stroke="#c9c9cb" stroke-width="1"/></svg>
          danawhitlow@BirchfordRealty.example
        </li>
        <li>
          <svg viewBox="0 0 22 22" aria-hidden="true"><circle cx="11" cy="11" r="9.5" fill="none" stroke="#1a1a1a" stroke-width="1.6"/><circle cx="11" cy="11" r="5.5" fill="none" stroke="#1a1a1a" stroke-width="1.2"/><path d="M5.5 11h11M11 5.5c-2.5 3-2.5 8 0 11M11 5.5c2.5 3 2.5 8 0 11" fill="none" stroke="#1a1a1a" stroke-width="1"/></svg>
          birchfordrealty.example
        </li>
      </ul>
      <div class="skyline" role="img" aria-label="City skyline illustration in blue"></div>
    </div>
    <div class="brand-panel">
      <p class="license">License No. : 5839162</p>
      <p class="brand-name">Birchford Realty</p>
      <p class="address">#7218 Crestover Ave E, Saginaw, MI 48271</p>
    </div>
  </section>

  <section class="card card--back" aria-label="Business card back">
    <svg class="back-curve" viewBox="0 0 700 400" preserveAspectRatio="none" aria-hidden="true">
      <path d="M0 280 C 200 250, 330 100, 700 45 L700 400 L0 400 Z" fill="#ffffff"/>
    </svg>
    <p class="back-brand">Birchford Realty</p>
    <div class="appt-field field-date">DATE :<span class="fill"></span></div>
    <div class="appt-field field-time">TIME :<span class="fill"></span></div>
    <div class="appt-field field-desc">DESCRIPTION :<span class="fill"></span></div>
    <div class="desc-line" style="top:232px;left:250px"></div>
    <div class="desc-line" style="top:292px"></div>
    <div class="desc-line" style="top:328px"></div>
    <div class="desc-line" style="top:364px"></div>
  </section>

</main>
</body>
</html>
```